automotive repair and collision repair shop card

our company is called K.R Motor service we are a automotive repair company
we also do government inspections. the company information is on the cards. I would like you to use my new logo and create a new card and use the information from my old card. Good Luck!!

Industry/Entity Type

Car Repair

Contact Information for Business Card

Address: #417-15862 91 Ave, Surrey, BC V5T 8K4
Phone:(604) 555-0187
fax 604 555 0142
website www.krmotor.example

Font styles to use
Serif
Sans Serif

Requirements
Must have
• all the information
Should not have
• the owner and there name

```html
<!DOCTYPE html>
<html lang="en">
<head>
<meta charset="utf-8">
<title>K.R Motor service – Business Card</title>
<link rel="stylesheet" href="https://fonts.googleapis.com/css2?family=Open+Sans:wght@400;600&display=swap">
<style>
  :root {
    --backdrop: #e4e2de;
    --ink: #151515;
    --ink-deep: #0b0b0b;
    --band-grey: #2c2c2d;
    --paper: #ececed;
    --paper-shade: #cfd0d2;
    --silver: #f4f4f4;
    --label: #e9e9e9;
    --illustration: #5a5b5d;
  }
  * { box-sizing: border-box; margin: 0; padding: 0; }
  html, body {
    width: 1200px; height: 900px; overflow: hidden;
    background: var(--backdrop);
    font-family: "Open Sans", Arial, sans-serif;
  }
  .stage { position: relative; width: 1200px; height: 900px; }
  .card {
    position: absolute; left: 290px; width: 620px; height: 354px;
    border-radius: 14px; overflow: hidden;
    box-shadow: 0 10px 24px rgba(0,0,0,.25);
  }
  .card--front { top: 70px; }
  .card--back { top: 476px; }
  .card__bg { position: absolute; inset: 0; width: 100%; height: 100%; }
  .logo-art {
    position: absolute; border-radius: 40px 60px 18px 18px;
    background: linear-gradient(180deg, #7a7b7d 0%, var(--illustration) 55%, #2a2a2b 100%);
  }
  .card--front .logo-art { left: 150px; top: 95px; width: 300px; height: 100px; }
  .card--back .logo-art { left: 200px; top: 42px; width: 220px; height: 72px; }
  .brand-name {
    position: absolute; left: 0; right: 0; text-align: center;
    font-weight: 600; color: var(--ink); letter-spacing: .5px;
  }
  .card--front .brand-name { top: 210px; font-size: 40px; }
  .card--back .brand-name { top: 120px; font-size: 28px; }
  .contact { position: absolute; list-style: none; color: var(--label); font-size: 15px; }
  .contact li { display: flex; align-items: center; gap: 12px; height: 26px; }
  .contact svg { width: 18px; height: 18px; flex: none; }
  .contact--phones { left: 420px; top: 210px; }
  .contact--online { left: 40px; top: 262px; }
  .address {
    position: absolute; left: 0; right: 0; top: 322px; text-align: center;
    color: var(--label); font-size: 15px; letter-spacing: .3px;
  }
</style>
</head>
<body>
<main class="stage">

  <section class="card card--front" aria-label="Card front">
    <svg class="card__bg" viewBox="0 0 620 354" preserveAspectRatio="none" aria-hidden="true">
      <defs>
        <linearGradient id="paperFront" x1="0" y1="0" x2="0" y2="1">
          <stop offset="0" stop-color="#f2f2f3"/>
          <stop offset="1" stop-color="#d4d5d7"/>
        </linearGradient>
      </defs>
      <rect width="620" height="354" fill="url(#paperFront)"/>
      <path d="M0 0 H620 V38 C480 62 300 52 0 74 Z" fill="var(--ink)"/>
      <path d="M0 74 C300 52 480 62 620 38" fill="none" stroke="var(--silver)" stroke-width="3"/>
    </svg>
    <div class="logo-art" role="img" aria-label="Logo illustration: side view of a sports car"></div>
    <p class="brand-name">K.R Motor service</p>
  </section>

  <section class="card card--back" aria-label="Card back">
    <svg class="card__bg" viewBox="0 0 620 354" preserveAspectRatio="none" aria-hidden="true">
      <defs>
        <linearGradient id="paperBack" x1="0" y1="0" x2="0" y2="1">
          <stop offset="0" stop-color="#f0f0f1"/>
          <stop offset="1" stop-color="#cfd0d2"/>
        </linearGradient>
      </defs>
      <rect width="620" height="354" fill="url(#paperBack)"/>
      <rect width="620" height="24" fill="var(--ink)"/>
      <path d="M0 205 C160 228 330 200 460 176 C540 164 590 170 620 172 V354 H0 Z" fill="var(--ink)"/>
      <path d="M0 205 C160 228 330 200 460 176 C540 164 590 170 620 172" fill="none" stroke="var(--silver)" stroke-width="3"/>
      <rect y="308" width="620" height="46" fill="var(--band-grey)"/>
    </svg>
    <div class="logo-art" role="img" aria-label="Logo illustration: side view of a sports car"></div>
    <p class="brand-name">K.R Motor service</p>

    <ul class="contact contact--phones">
      <li>
        <svg viewBox="0 0 20 20" aria-hidden="true"><rect x="2" y="7" width="16" height="8" rx="2" fill="var(--label)"/><rect x="5" y="3" width="10" height="5" fill="var(--label)"/><rect x="5" y="13" width="10" height="5" fill="var(--label)" stroke="var(--ink)" stroke-width="1"/></svg>
        <span>604 555 0142</span>
      </li>
      <li>
        <svg viewBox="0 0 20 20" aria-hidden="true"><path d="M5 2 L8 2 L9 6 L7 8 C8 11 9 12 12 13 L14 11 L18 12 L18 15 C18 17 16 18 14 18 C8 17 3 12 2 6 C2 4 3 2 5 2 Z" fill="var(--label)"/></svg>
        <span>(604) 555-0187</span>
      </li>
    </ul>

    <ul class="contact contact--online">
      <li>
        <svg viewBox="0 0 20 20" aria-hidden="true"><rect x="1.5" y="4" width="17" height="12" fill="none" stroke="var(--label)" stroke-width="1.5"/><path d="M1.5 4 L10 11 L18.5 4" fill="none" stroke="var(--label)" stroke-width="1.5"/></svg>
        <span>info@krmotor.example</span>
      </li>
      <li>
        <svg viewBox="0 0 20 20" aria-hidden="true"><circle cx="10" cy="10" r="8" fill="none" stroke="var(--label)" stroke-width="1.5"/><ellipse cx="10" cy="10" rx="3.5" ry="8" fill="none" stroke="var(--label)" stroke-width="1.2"/><path d="M2 10 H18 M3.5 6 H16.5 M3.5 14 H16.5" stroke="var(--label)" stroke-width="1.2"/></svg>
        <span>www.krmotor.example</span>
      </li>
    </ul>

    <p class="address">#417-15862 91 Ave, Surrey, BC V5T 8K4</p>
  </section>

</main>
</body>
</html>
```